Copperfen Hollow Wine And Spirits

We need to design a website for our Liquor Store

Industry/Entity Type

Store

Number of Pages Required

4 page

Requirements
Must have
• Beer, Liquor, Wine & Cigar related theme.
• Mention our 8-locations addresses & maps info
Nice to have
• category for Beer, Liquor & Wine to setup database for item list to link our sql server database.

```html
<!DOCTYPE html>
<html lang="en">
<head>
<meta charset="utf-8">
<title>Copperfen Hollow Wine And Spirits</title>
<link href="https://fonts.googleapis.com/css2?family=Montserrat:wght@400;500;600;700&family=Open+Sans:wght@400;600&display=swap" rel="stylesheet">
<style>
:root{
  --navy:#1b3f8e;
  --gold:#e39b00;
  --green:#4aab1f;
  --ink:#2b2b2b;
  --muted:#666;
  --page:#f1f1f1;
  --white:#fff;
  --dark:#262626;
  --line:#d6d6d6;
}
*{margin:0;padding:0;box-sizing:border-box}
html,body{width:1200px;height:3455px;overflow:hidden}
body{position:relative;background:var(--page);font-family:"Open Sans",Arial,sans-serif;color:var(--ink)}
.abs{position:absolute}
.btn{position:absolute;display:flex;align-items:center;justify-content:center;border:2px solid var(--navy);border-radius:18px;font:600 12px "Montserrat",Arial,sans-serif;color:var(--navy);background:var(--white)}
.btn.solid{background:var(--navy);color:var(--white)}
.photo{position:absolute}

/* top bar */
.topbar{left:0;top:0;width:1200px;height:28px;background:#f7f7f7;border-bottom:1px solid #e4e4e4;font-size:11px;color:#555}
.topbar .promo{left:154px;top:7px}
.topbar .account{left:735px;top:7px}
.social{display:flex;gap:5px}
.social span{width:15px;height:15px;border-radius:50%;background:#555;display:block}

/* header */
.header{left:0;top:28px;width:1200px;height:87px;background:var(--white)}
.logo{left:154px;top:26px;display:flex;align-items:center;gap:8px;font:700 15px "Montserrat",Arial,sans-serif;color:var(--ink);line-height:1.2;width:190px}
.logo i{width:14px;height:14px;border-radius:50%;background:var(--green);flex:none}
.nav a{position:absolute;top:35px;font:500 12px "Montserrat",Arial,sans-serif;color:#666;text-decoration:none}
.nav a.active{color:var(--navy)}
.cart{left:900px;top:28px;display:flex;gap:8px;font-size:11px;color:#666}
.cart b{color:var(--navy)}

/* hero */
.hero{left:0;top:115px;width:1200px;height:514px;background:radial-gradient(ellipse at 70% 40%,#9b3a1c 0%,#5e1a0e 45%,#2a0a05 100%)}
.hero .kicker{left:230px;top:160px;font:600 16px "Montserrat",Arial,sans-serif;color:var(--gold)}
.hero h1{left:230px;top:190px;font:600 44px "Montserrat",Arial,sans-serif;color:var(--white)}
.hero p{left:230px;top:254px;width:420px;font-size:13px;line-height:19px;color:#f0e2dc}
.hero .bottles{left:680px;top:95px;width:280px;height:345px;background:linear-gradient(90deg,#1a0d08,#3a1410 50%,#5a1018);border-radius:6px;opacity:.85}
.hero .arrow{top:240px}

/* categories */
.cat{top:656px;width:279px;height:157px;overflow:hidden}
.cat .photo{inset:0}
.cat .title{right:18px;top:38px;text-align:right;font:700 16px "Montserrat",Arial,sans-serif;color:var(--gold)}
.cat .title span{display:block;font-size:13px;color:var(--white);font-weight:600}
.cat .tab{right:0;bottom:0;width:105px;height:30px;background:var(--green);clip-path:polygon(18% 0,100% 0,100% 100%,0 100%);font:700 11px "Montserrat",Arial,sans-serif;color:var(--white);display:flex;align-items:center;justify-content:flex-end;padding-right:14px}
.cat .tab.blue{background:var(--navy)}

/* welcome */
.welcome-photo{left:154px;top:875px;width:459px;height:401px;background:linear-gradient(135deg,#c9a27a,#8a5a36 55%,#4b3022)}
.welcome .small{left:663px;top:942px;font:500 13px "Montserrat",Arial,sans-serif}
.welcome h2{left:663px;top:964px;font:600 22px "Montserrat",Arial,sans-serif;color:var(--gold)}
.welcome p{left:663px;width:380px;font-size:11px;line-height:18px;color:var(--muted)}

/* products */
.section-kicker{font:500 13px "Montserrat",Arial,sans-serif}
.section-title{font:600 22px "Montserrat",Arial,sans-serif;color:var(--gold)}
.filters{left:703px;top:1356px;display:flex;gap:12px;font:600 11px "Montserrat",Arial,sans-serif;color:#333}
.filters em{font-style:normal;color:#bbb}
.card{top:1416px;width:203px;height:330px;background:var(--white);box-shadow:0 0 0 1px #e8e8e8}
.card.raised{box-shadow:0 4px 14px rgba(0,0,0,.15)}
.card .photo{left:10px;top:7px;width:183px;height:189px;background:linear-gradient(180deg,#f3f3f3,#e2e2e2)}
.card .name{top:218px;width:100%;text-align:center;font-size:12px;line-height:19px}
.card .price{top:266px;width:100%;text-align:center;font:600 20px "Montserrat",Arial,sans-serif;color:var(--green)}

/* promo banner */
.banner{left:154px;top:1822px;width:889px;height:200px;background:linear-gradient(90deg,#141414 0%,#1e1a16 45%,#5a3a1f 75%,#2a1a0e 100%)}
.banner .t1{left:76px;top:34px;font:400 28px "Montserrat",Arial,sans-serif;color:var(--green)}
.banner .t2{left:76px;top:72px;font:600 22px "Montserrat",Arial,sans-serif;color:var(--white)}

/* news */
.news{top:2158px;width:433px;height:161px;background:var(--white)}
.news .photo{left:0;top:0;width:180px;height:161px}
.news .date{left:195px;top:24px;font:500 13px "Montserrat",Arial,sans-serif;color:var(--green)}
.news .text{left:195px;top:48px;width:220px;font-size:12px;line-height:19px;color:#444}
.circle-arrow{width:30px;height:30px;border-radius:50%;display:flex;align-items:center;justify-content:center}

/* newsletter */
.newsletter{left:0;top:2448px;width:1200px;height:240px}
.newsletter-bg{inset:0;background:linear-gradient(90deg,#2b1d12,#4d3a24 30%,#6a4f2e 50%,#3e2c1a 75%,#1f150d)}
.newsletter-kicker{left:0;top:62px;width:1200px;text-align:center;font:600 13px "Montserrat",Arial,sans-serif;color:var(--white)}
.newsletter-title{left:0;top:84px;width:1200px;text-align:center;font:600 22px "Montserrat",Arial,sans-serif;color:var(--gold)}
.signup-input{left:382px;top:156px;width:325px;height:34px;background:var(--white);border-radius:17px 0 0 17px;font-size:11px;color:#888;padding:10px 18px}
.signup-button{left:707px;top:156px;width:111px;height:34px;background:var(--green);border-radius:0 17px 17px 0;font:600 11px "Montserrat",Arial,sans-serif;color:var(--white);display:flex;align-items:center;justify-content:center}

/* contact */
.contact{top:2688px;height:272px;width:1200px;left:0;background:var(--page)}
.info{top:88px;width:300px;text-align:center}
.info .label{margin-top:16px;font:600 12px "Montserrat",Arial,sans-serif}
.info .value{margin-top:4px;font-size:12px;line-height:18px;color:#555}
.divider{top:80px;width:1px;height:140px;background:var(--line)}

.map{left:0;top:2960px;width:1200px;height:430px;background:linear-gradient(135deg,#eef0e8,#e4e6dc 50%,#eaece4)}

.footer{left:0;top:3390px;width:1200px;height:65px;background:var(--dark);font-size:11px;color:#ccc}
</style>
</head>
<body>

<div class="abs topbar">
  <div class="abs promo">Extra 25%-40% Off Clearance</div>
  <div class="abs account">Welcome User &nbsp;|&nbsp; Login / Register</div>
  <div class="abs social" style="left:946px;top:6px"><span></span><span></span><span></span><span></span><span></span></div>
</div>

<header class="abs header">
  <div class="abs logo"><i></i>Copperfen Hollow Wine And Spirits</div>
  <nav class="nav">
    <a class="active" style="left:449px">Home</a>
    <a style="left:522px">About</a>
    <a style="left:598px">Products</a>
    <a style="left:682px">News</a>
    <a style="left:756px">Contact Us</a>
  </nav>
  <svg class="abs" style="left:860px;top:35px" width="16" height="16" viewBox="0 0 16 16" fill="none" stroke="#777" stroke-width="2"><circle cx="7" cy="7" r="5"/><path d="M11 11l4 4"/></svg>
  <div class="abs cart">
    <svg width="26" height="26" viewBox="0 0 26 26"><circle cx="13" cy="13" r="13" fill="#1b3f8e"/><path d="M7 8h2l2 8h7l2-6H10" fill="none" stroke="#fff" stroke-width="1.6"/><circle cx="12" cy="19" r="1.3" fill="#fff"/><circle cx="17" cy="19" r="1.3" fill="#fff"/></svg>
    <div>Shopping Cart<br>Item(s) 00 - <b>$0.00</b></div>
  </div>
</header>

<section class="abs hero">
  <div class="abs kicker">Buy Your</div>
  <h1 class="abs">Perfect Wine</h1>
  <p class="abs">There are many variations of passages of Lorem Ipsum available, but the majority have suffered...</p>
  <div class="btn solid" style="left:230px;top:318px;width:115px;height:34px">Shop Now!</div>
  <div class="photo bottles" role="img" aria-label="Three wine bottles"></div>
  <svg class="abs arrow" style="left:156px" width="20" height="40" viewBox="0 0 20 40" fill="none" stroke="#fff" stroke-width="2"><path d="M18 2L2 20l16 18"/></svg>
  <svg class="abs arrow" style="left:1024px" width="20" height="40" viewBox="0 0 20 40" fill="none" stroke="#fff" stroke-width="2"><path d="M2 2l16 18L2 38"/></svg>
</section>

<div class="abs cat" style="left:154px">
  <div class="photo" role="img" aria-label="Beer bottle and glass" style="background:linear-gradient(90deg,#3a2a22,#7a3a2a 55%,#a8562f)"></div>
  <div class="abs title">Beer<span>New Arrivals</span></div>
  <div class="abs tab">Shop Now!</div>
</div>
<div class="abs cat" style="left:461px">
  <div class="photo" role="img" aria-label="Man smoking a cigar" style="background:linear-gradient(90deg,#1a1a1a,#333 50%,#141414)"></div>
  <div class="abs title">Cigar<span>Mauris Justo</span></div>
  <div class="abs tab blue">Shop Now!</div>
</div>
<div class="abs cat" style="left:765px">
  <div class="photo" role="img" aria-label="Wine bottles with grapes" style="background:linear-gradient(90deg,#e8e4dc,#c9b9a4 55%,#8a5a3a)"></div>
  <div class="abs title">Wine<span>Extra 25% off</span></div>
  <div class="abs tab">Shop Now!</div>
</div>

<section class="welcome">
  <div class="photo welcome-photo" role="img" aria-label="Friends sharing drinks at a bar table"></div>
  <div class="abs small">Welcome to</div>
  <h2 class="abs">Copperfen Hollow</h2>
  <p class="abs" style="top:1008px">Lorem Ipsum is simply dummy text of the printing and typesetting industry. Lorem Ipsum has been the industry's standard dummy text ever since the 1500s, when an unknown printer took a galley of type and scrambled it to make a type specimen book.</p>
  <p class="abs" style="top:1108px">It has survived not only five centuries, but also the leap into electronic typesetting, remaining essentially unchanged....</p>
  <div class="btn" style="left:663px;top:1176px;width:130px;height:32px">Discover More</div>
</section>

<section class="products">
  <div class="abs section-kicker" style="left:154px;top:1337px">Shop Now!</div>
  <div class="abs section-title" style="left:154px;top:1358px">Our Products</div>
  <div class="abs filters"><span>Beer</span><em>|</em><span>Liquor</span><em>|</em><span style="color:var(--navy)">Wine</span><em>|</em><span>Cigar</span></div>
  <div class="btn" style="left:937px;top:1348px;width:106px;height:32px">View All</div>

  <div class="abs card" style="left:154px"><div class="photo" role="img" aria-label="Red wine bottle"></div><div class="abs name">Redmarsh Vale<br>Zinfandel</div><div class="abs price">$43.18</div><div class="btn" style="left:47px;top:307px;width:110px;height:30px">Shop Now!</div></div>
  <div class="abs card raised" style="left:385px"><div class="photo" role="img" aria-label="White wine bottle"></div><div class="abs name">Redmarsh Vale<br>Zinfandel</div><div class="abs price">$43.18</div><div class="btn solid" style="left:47px;top:307px;width:110px;height:30px">Shop Now!</div></div>
  <div class="abs card" style="left:615px"><div class="photo" role="img" aria-label="White wine bottle"></div><div class="abs name">Redmarsh Vale<br>Zinfandel</div><div class="abs price">$43.18</div><div class="btn" style="left:47px;top:307px;width:110px;height:30px">Shop Now!</div></div>
  <div class="abs card" style="left:843px"><div class="photo" role="img" aria-label="Red wine bottle"></div><div class="abs name">Redmarsh Vale<br>Zinfandel</div><div class="abs price">$43.18</div><div class="btn" style="left:47px;top:307px;width:110px;height:30px">Shop Now!</div></div>
</section>

<section class="abs banner" role="img" aria-label="Whisky glasses and a cigar on a dark table">
  <div class="abs t1">The Big Brands Event</div>
  <div class="abs t2">Up to 50% off</div>
  <div class="btn" style="left:76px;top:128px;width:130px;height:30px;background:transparent;border-color:#fff;color:#fff">Explore More</div>
</section>

<section class="news-section">
  <div class="abs section-kicker" style="left:154px;top:2083px">Recent Update</div>
  <div class="abs section-title" style="left:154px;top:2104px">Latest News</div>
  <div class="abs circle-arrow" style="left:971px;top:2095px;background:var(--green)"><svg width="10" height="10" viewBox="0 0 10 10" fill="none" stroke="#fff" stroke-width="2"><path d="M7 1L3 5l4 4"/></svg></div>
  <div class="abs circle-arrow" style="left:1013px;top:2095px;background:var(--navy)"><svg width="10" height="10" viewBox="0 0 10 10" fill="none" stroke="#fff" stroke-width="2"><path d="M3 1l4 4-4 4"/></svg></div>

  <article class="abs news" style="left:154px">
    <div class="photo" role="img" aria-label="Wine glasses with grapes" style="background:linear-gradient(135deg,#5a3a1a,#b07a2a 50%,#3a4a1a)"></div>
    <div class="abs date">30-Sept -2017</div>
    <div class="abs text">There are many variations of passages of Lorem...</div>
    <div class="btn" style="left:195px;top:111px;width:110px;height:30px">Read More</div>
  </article>
  <article class="abs news" style="left:610px">
    <div class="photo" role="img" aria-label="Man tasting red wine" style="background:linear-gradient(135deg,#2a1a14,#7a4a34 50%,#3a2218)"></div>
    <div class="abs date">30-Sept -2017</div>
    <div class="abs text">There are many variations of passages of Lorem...</div>
    <div class="btn solid" style="left:195px;top:111px;width:110px;height:30px">Read More</div>
  </article>
  <div class="btn" style="left:548px;top:2353px;width:108px;height:32px">View All</div>
</section>

<section class="abs newsletter">
  <div class="abs newsletter-bg" role="img" aria-label="Wine barrels and bottles in a cellar"></div>
  <div class="abs newsletter-kicker">Subscribe</div>
  <div class="abs newsletter-title">Our Newsletter</div>
  <div class="abs signup-input">Enter Your Email...</div>
  <div class="abs signup-button">Subscribe</div>
</section>

<section class="abs contact">
  <div class="abs info" style="left:144px">
    <svg width="34" height="34" viewBox="0 0 34 34" fill="none" stroke="#777" stroke-width="1.6"><path d="M8 4l6 6-3 4c2 4 5 7 9 9l4-3 6 6-4 4C15 30 4 19 4 8z"/></svg>
    <div class="label">Call Us:</div>
    <div class="value" style="font:600 15px 'Montserrat',Arial,sans-serif;color:var(--navy)">123 - 456 - 7890</div>
  </div>
  <div class="abs divider" style="left:445px"></div>
  <div class="abs info" style="left:448px">
    <svg width="34" height="34" viewBox="0 0 34 34" fill="none" stroke="#777" stroke-width="1.6"><path d="M17 32S6 20 6 13a11 11 0 0122 0c0 7-11 19-11 19z"/><circle cx="17" cy="13" r="4"/></svg>
    <div class="label">Locations:</div>
    <div class="value">4518 Alder Creek Rd, Fenwick<br>- MO 33537</div>
  </div>
  <div class="abs divider" style="left:751px"></div>
  <div class="abs info" style="left:754px">
    <svg width="40" height="34" viewBox="0 0 40 34" fill="none" stroke="#777" stroke-width="1.6"><rect x="3" y="5" width="34" height="24"/><path d="M3 5l17 14L37 5"/></svg>
    <div class="label">Email Us:</div>
    <div class="value" style="color:var(--navy);text-decoration:underline">info@copperfenhollow.com</div>
  </div>
</section>

<div class="abs map" role="img" aria-label="Street map showing the store location"></div>

<footer class="abs footer">
  <div class="abs" style="left:154px;top:26px">© 2017 <span style="color:var(--navy)">Copperfen Hollow</span>. All Right Reserved. &nbsp;&nbsp;&nbsp; Terms of Use &nbsp;|&nbsp; Privacy Policy</div>
  <div class="abs" style="left:820px;top:26px">Get Social:</div>
  <div class="abs social" style="left:888px;top:25px"><span></span><span></span><span></span><span></span><span></span></div>
  <svg class="abs" style="left:1030px;top:26px" width="12" height="12" viewBox="0 0 12 12" fill="none" stroke="#3a63c4" stroke-width="2"><path d="M1 8l5-5 5 5"/></svg>
</footer>

</body>
</html>
```